RTV Business Card

We need a new design for our business cards. We are brokers in the scrap metal industry and wants something nice, clean and very professional.

Industry/Entity Type

Business

Requirements
Must have
• Our logo
• Would probably be good to incorporate colors from logo into design.
• Example info we need on the cards.
• Name
• Company Address
• Cell Phone
• Office Phone
• Fax
• Email
• Company Website
Should not have
• Should not be too cluttered. Needs to be nice, clean and professional looking.

```html
<!DOCTYPE html>
<html lang="en">
<head>
<meta charset="utf-8">
<title>RTV Business Card</title>
<link href="https://fonts.googleapis.com/css2?family=Barlow:wght@300;400;600;700&display=swap" rel="stylesheet">
<style>
  :root {
    --page: #e4e2de;
    --card: #f4f4f3;
    --ink: #3a3a3a;
    --ink-soft: #555;
    --brand-red: #c1272d;
    --brand-blue: #1f6fa9;
    --brand-navy: #17395e;
  }
  * { box-sizing: border-box; margin: 0; padding: 0; }
  html, body {
    width: 1200px;
    height: 900px;
    overflow: hidden;
  }
  body {
    background: var(--page);
    font-family: "Barlow", sans-serif;
    color: var(--ink);
    display: flex;
    flex-direction: column;
    align-items: center;
    justify-content: center;
    gap: 44px;
  }
  .card {
    position: relative;
    width: 560px;
    height: 320px;
    background: var(--card);
    box-shadow: 0 2px 10px rgba(0,0,0,0.12);
  }
  .card__stripe {
    position: absolute;
    left: 0;
    right: 0;
    bottom: 22px;
    height: 7px;
    background: linear-gradient(90deg, var(--brand-blue), var(--brand-navy));
  }
  .brand-mark {
    display: flex;
    align-items: center;
    gap: 10px;
  }
  .brand-mark__square {
    width: 22px;
    height: 22px;
    background: var(--brand-red);
  }
  .brand-mark__name {
    font-weight: 700;
    color: var(--brand-navy);
    letter-spacing: 0.04em;
  }

  /* Front */
  .card--front .front__content {
    position: absolute;
    left: 0;
    right: 0;
    top: 70px;
    display: flex;
    flex-direction: column;
    align-items: center;
  }
  .card--front .brand-mark__name { font-size: 56px; line-height: 1; }
  .front__company {
    margin-top: 14px;
    font-size: 24px;
    font-weight: 700;
    color: #2b2b2b;
  }
  .front__website {
    margin-top: 26px;
    font-size: 15px;
    color: var(--brand-blue);
    letter-spacing: 0.03em;
  }

  /* Back */
  .card--back .back__mark {
    position: absolute;
    left: 46px;
    top: 120px;
  }
  .card--back .brand-mark__name { font-size: 50px; line-height: 1; }
  .back__details {
    position: absolute;
    left: 250px;
    top: 48px;
  }
  .back__name {
    font-size: 22px;
    font-weight: 400;
    letter-spacing: 0.05em;
    text-transform: uppercase;
  }
  .back__title {
    font-size: 13px;
    color: var(--ink-soft);
    margin-top: 2px;
  }
  .contact-list {
    list-style: none;
    margin-top: 34px;
    font-size: 15px;
    line-height: 21px;
    font-weight: 300;
    color: var(--ink);
  }
  .contact-list__label {
    display: inline-block;
    width: 18px;
    color: var(--brand-red);
    font-weight: 400;
  }
  .back__address {
    font-size: 15px;
    line-height: 21px;
    font-weight: 300;
    margin-left: 18px;
  }
  .back__website {
    margin-top: 12px;
    font-size: 15px;
    color: var(--brand-blue);
  }
</style>
</head>
<body>

  <section class="card card--front" aria-label="Business card front">
    <div class="front__content">
      <div class="brand-mark">
        <span class="brand-mark__square"></span>
        <span class="brand-mark__name">RTV</span>
      </div>
      <p class="front__company">Rivet Trade Ventures</p>
      <p class="front__website">www.rivettradeventures.com</p>
    </div>
    <div class="card__stripe"></div>
  </section>

  <section class="card card--back" aria-label="Business card back">
    <div class="back__mark brand-mark">
      <span class="brand-mark__square"></span>
      <span class="brand-mark__name">RTV</span>
    </div>
    <div class="back__details">
      <h1 class="back__name">Dana Whitfield</h1>
      <p class="back__title">Director</p>
      <ul class="contact-list">
        <li><span class="contact-list__label">T</span>(555) 210-4830</li>
        <li><span class="contact-list__label">F</span>(555) 210-4831</li>
        <li><span class="contact-list__label">E</span>info@rivettradeventures.com</li>
      </ul>
      <p class="back__address">2740 Harbor Ave.<br>East Linwood, SC 29000</p>
      <p class="back__website">www.rivettradeventures.com</p>
    </div>
    <div class="card__stripe"></div>
  </section>

</body>
</html>
```